Norvale Email Signature Banners – Fabrication Capability Series

www.Norvale.com.au is an Australian engineering and fabrication company specialising in fabrication and welding of :
steel piping spools,
skids and frames,
small volume process steel tanks
and general steel fabrication
We require four distinct banner designs for use in Teldrin Quillmark email signatures. Each banner will highlight a specific capability while maintaining a consistent brand identity.
Deliverables
Four banners total:
Piping Spools Fabrication – focus on precision welding and stainless steel pipework
Skid & Frames Fabrication – highlight skid systems and structural frames
Small Steel Tanks Fabrication – show fabricated tanks and workshop craftsmanship
General Fabrication Solutions – broad steel fabrication theme for company-wide use
Dimensions: 600–700 px wide × 100 px high
Format: PNG (preferred), small file size prefered
Resolution: 72 dpi
Background: non-transparent, industrial or workshop setting
Text examples:
1. Piping Spools Fabrication
Option A: “Expert Fabrication Solutions for Process Piping”
Option B: “Precision Welding for Complex Systems”
Option C: “Delivering Quality in Every Spool”
Option D: “Engineered for Flow, Built for Strength”
2. Skid & Frames Fabrication
Option A: “Custom Engineered Modular Systems”
Option B: “Built Strong. Designed Smart.”
Option C: “Reliable Frames for Industrial Performance”
Option D: “Modular Fabrication for Seamless Integration”
3. Small Steel Tanks Fabrication
Option A: “Precision Built for Your Needs”
Option B: “Compact Strength. Proven Durability.”
Option C: “Fabricated for Performance and Longevity”
Option D: “Small Tanks. Big Reliability.”
4. General Fabrication Solutions
Option A: “Quality Craftsmanship, Proven Results”
Option B: “Your Partner in Precision Fabrication”
Option C: “Engineering Excellence in Every Weld”
Option D: “Australian Fabrication. Global Standards.”
Style Direction
Clean, professional, and engineering‑focused
Use Norvale brand colours
Blend photo realism with vector clarity (no heavy gradients)
Include subtle industrial textures or workshop imagery
Typography: bold sans‑serif, legible at small scale
Usage Context
These banners will appear at the bottom of staff email signatures via Quillmark Email Signature Tool for Teldrin 365, so clarity and fast loading are essential. No Logo is required in the banners.
Reference
Existing Norvale signature is attached. Colour palette to match the signature style and logo.
Target Market(s)
Engineering and construction companies,
Industry/Entity Type
Engineering fabrication design

```html
<!DOCTYPE html>
<html lang="en">
<head>
<meta charset="utf-8">
<title>Norvale Email Signature Banners</title>
<link rel="stylesheet" href="https://fonts.googleapis.com/css2?family=Arimo:ital,wght@0,400;0,700;1,700&display=swap">
<style>
:root{
  --canvas:#e2e2e2;
  --white:#ffffff;
  --navy:#0f2f66;
  --deep-blue:#14489a;
  --brand-blue:#1a5fc4;
  --sky-blue:#2aa6e2;
  --logo-blue:#2c9bd6;
  --steel:#5d7fae;
}
*{box-sizing:border-box;margin:0;padding:0}
html,body{width:1200px;height:900px;overflow:hidden}
body{background:var(--canvas);font-family:"Arimo",Arial,sans-serif;position:relative}
.banner{position:absolute;left:57px;width:1086px;height:155px;overflow:hidden;background:var(--white);box-shadow:0 3px 6px rgba(0,0,0,.35)}
.banner--skid{top:60px}
.banner--tanks{top:270px}
.banner--general{top:480px}
.banner--spools{top:688px}
.banner svg.backdrop{position:absolute;inset:0;width:100%;height:100%}
.brand{position:absolute;left:40px;top:58px;display:flex;align-items:center;gap:8px;font-weight:700;font-size:27px;letter-spacing:1px;color:var(--logo-blue)}
.brand__mark{width:18px;height:18px;background:var(--logo-blue)}
.headline{position:absolute;color:var(--white);font-weight:700;text-transform:uppercase;line-height:1.02;white-space:nowrap}
.address{position:absolute;color:var(--white);font-weight:700;font-size:17px;white-space:nowrap}
.divider{position:absolute;width:2px;background:var(--white);top:22px;height:112px}
.contact{position:absolute;color:var(--white);font-weight:700;white-space:nowrap}
.contact__tagline{font-size:17px;line-height:1.2;text-transform:uppercase;margin-bottom:6px}
.contact__row{display:flex;font-size:15px;line-height:1.22}
.contact__label{width:58px}
.contact__sep{width:22px}
.contact__address{font-style:italic;font-size:15px;margin-top:2px}
</style>
</head>
<body>

<section class="banner banner--skid">
  <svg class="backdrop" viewBox="0 0 1086 155" preserveAspectRatio="none" role="img" aria-label="Workshop photo of skid systems and structural frames, tinted dark blue">
    <defs>
      <linearGradient id="skid-photo" x1="0" y1="0" x2="1" y2="0">
        <stop offset="0" stop-color="#143d7e"/><stop offset=".55" stop-color="#2b5a98"/><stop offset="1" stop-color="#123a78"/>
      </linearGradient>
    </defs>
    <polygon points="262,0 1086,0 1086,155 248,155" fill="url(#skid-photo)"/>
  </svg>
  <div class="brand"><span class="brand__mark"></span>NORVALE</div>
  <h2 class="headline" style="left:288px;top:14px;font-size:46px">Skid &amp; Frames<br>Fabrication</h2>
  <p class="address" style="left:288px;top:118px">14-18 Ironbark Road, Kelmscott Vale, WA 6199</p>
  <span class="divider" style="left:708px"></span>
  <div class="contact" style="left:744px;top:20px">
    <p class="contact__tagline">Custom Engineered Modular<br>Systems</p>
    <p class="contact__row"><span class="contact__label">Mobile</span><span class="contact__sep">:</span>+61 XXX 731 486</p>
    <p class="contact__row"><span class="contact__label">Web</span><span class="contact__sep">:</span>http://www.norvale.com.au</p>
    <p class="contact__row"><span class="contact__label">Email</span><span class="contact__sep">:</span>STAFF@norvale.com.au</p>
  </div>
</section>

<section class="banner banner--tanks">
  <svg class="backdrop" viewBox="0 0 1086 155" preserveAspectRatio="none" role="img" aria-label="Workshop photo of fabricated steel tanks, tinted blue">
    <defs>
      <linearGradient id="tanks-photo" x1="0" y1="0" x2="1" y2="0">
        <stop offset="0" stop-color="#2a5c9c"/><stop offset=".6" stop-color="#4670a8"/><stop offset="1" stop-color="#1d54a6"/>
      </linearGradient>
      <linearGradient id="tanks-pill" x1="0" y1="0" x2="1" y2="0">
        <stop offset="0" stop-color="#27a4e4"/><stop offset=".7" stop-color="#2a8fd2" stop-opacity=".9"/><stop offset="1" stop-color="#2a7fc4" stop-opacity="0"/>
      </linearGradient>
    </defs>
    <rect x="250" y="0" width="836" height="155" fill="url(#tanks-photo)"/>
    <path d="M300,0 H780 V155 H300 A77.5,77.5 0 0 1 300,0 Z" fill="url(#tanks-pill)"/>
  </svg>
  <div class="brand"><span class="brand__mark"></span>NORVALE</div>
  <h2 class="headline" style="left:295px;top:16px;font-size:40px">Small Steel<br>Tanks Fabrication</h2>
  <p class="address" style="left:295px;top:112px">14-18 Ironbark Road, Kelmscott Vale, WA 6199</p>
  <span class="divider" style="left:753px"></span>
  <div class="contact" style="left:783px;top:22px">
    <p class="contact__tagline">Precision Built for<br>Your Needs</p>
    <p class="contact__row"><span class="contact__label">Mobile</span><span class="contact__sep">:</span>+61 XXX 731 486</p>
    <p class="contact__row"><span class="contact__label">Web</span><span class="contact__sep">:</span>http://www.norvale.com.au</p>
    <p class="contact__row"><span class="contact__label">Email</span><span class="contact__sep">:</span>STAFF@norvale.com.au</p>
  </div>
</section>

<section class="banner banner--general">
  <svg class="backdrop" viewBox="0 0 1086 155" preserveAspectRatio="none" role="img" aria-label="Workshop photo of a general steel fabrication floor, fading from white into blue">
    <defs>
      <linearGradient id="general-photo" x1="0" y1="0" x2="1" y2="0">
        <stop offset="0" stop-color="#ffffff"/><stop offset=".17" stop-color="#ffffff"/><stop offset=".27" stop-color="#4d6f9e"/><stop offset="1" stop-color="#2f5a92"/>
      </linearGradient>
    </defs>
    <rect width="1086" height="155" fill="url(#general-photo)"/>
    <path d="M660,0 H1086 V155 H700 C740,110 690,40 660,0 Z" fill="var(--brand-blue)"/>
  </svg>
  <div class="brand"><span class="brand__mark"></span>NORVALE</div>
  <h2 class="headline" style="left:306px;top:8px;font-size:43px;font-style:italic">General<br>Fabrication<br>Solutions</h2>
  <div class="contact" style="left:718px;top:18px">
    <p class="contact__tagline" style="margin-bottom:3px">Quality Craftsmanship, Proven<br>Results</p>
    <p class="contact__row"><span class="contact__label">Mobile</span><span class="contact__sep">:</span>+61 XXX 731 486</p>
    <p class="contact__row"><span class="contact__label">Web</span><span class="contact__sep">:</span>http://www.norvale.com.au</p>
    <p class="contact__row"><span class="contact__label">Email</span><span class="contact__sep">:</span>STAFF@norvale.com.au</p>
    <p class="contact__address">14-18 Ironbark Road, Kelmscott Vale, WA 6199</p>
  </div>
</section>

<section class="banner banner--spools">
  <svg class="backdrop" viewBox="0 0 1086 155" preserveAspectRatio="none" role="img" aria-label="Workshop photo of welded piping spools, fading from white into blue">
    <defs>
      <linearGradient id="spools-photo" x1="0" y1="0" x2="1" y2="0">
        <stop offset="0" stop-color="#ffffff"/><stop offset=".15" stop-color="#ffffff"/><stop offset=".24" stop-color="#5a7cab"/><stop offset="1" stop-color="#35639c"/>
      </linearGradient>
      <linearGradient id="spools-panel" x1="0" y1="0" x2="1" y2="0">
        <stop offset="0" stop-color="#2a8fd8"/><stop offset="1" stop-color="#1557bf"/>
      </linearGradient>
    </defs>
    <rect width="1086" height="155" fill="url(#spools-photo)"/>
    <path d="M720,0 H1086 V155 H600 C660,140 680,30 720,0 Z" fill="url(#spools-panel)"/>
  </svg>
  <div class="brand"><span class="brand__mark"></span>NORVALE</div>
  <h2 class="headline" style="left:253px;top:12px;font-size:46px">Piping Spools<br>Fabrication</h2>
  <p class="address" style="left:253px;top:118px">14-18 Ironbark Road, Kelmscott Vale, WA 6199</p>
  <div class="contact" style="left:732px;top:20px">
    <p class="contact__tagline">Expert Fabrication Solutions<br>for Process Piping</p>
    <p class="contact__row"><span class="contact__label">Mobile</span><span class="contact__sep">:</span>+61 XXX 731 486</p>
    <p class="contact__row"><span class="contact__label">Web</span><span class="contact__sep">:</span>http://www.norvale.com.au</p>
    <p class="contact__row"><span class="contact__label">Email</span><span class="contact__sep">:</span>STAFF@norvale.com.au</p>
  </div>
</section>

</body>
</html>
```